Road Construction Company needs business cards

We would like a new business card designed for our business.

We're a road construction company based in Qld, Australia.

Can the business card please have the following information on it.

Name: Brent Malvoy
Position: General Manager
Phone: 0471 592 304
Email: Brent.malvoy@quendix.com.au
Address: 87 Harrowgate Ave, Pindarra, QLD, 4000
Website: www.quendix.com.au

Visually we'd like the card to be professional and simple.

Attached is our logo.

Our website is www.quendix.com.au

Target Market(s)

Men aged 25-60

Contact Information for Business Card

As listed in project description

Font styles to use
Serif

Requirements
Must have
• Large logo on back of card

```html
<!DOCTYPE html>
<html lang="en">
<head>
<meta charset="utf-8">
<title>Quendix Business Card</title>
<link rel="stylesheet" href="https://fonts.googleapis.com/css2?family=Noto+Serif:wght@400;700&display=swap">
<style>
  :root {
    --brand-blue: #0452a0;
    --brand-light: #35a4dc;
    --ink: #2e2e2e;
    --card: #ffffff;
    --backdrop: #d9d8d5;
  }
  * { margin: 0; padding: 0; box-sizing: border-box; }
  html, body { width: 1200px; height: 801px; overflow: hidden; }
  body {
    background: var(--backdrop);
    font-family: "Noto Serif", Georgia, serif;
    display: flex;
    align-items: center;
    justify-content: center;
    gap: 44px;
  }
  .card {
    position: relative;
    width: 540px;
    height: 310px;
    background: var(--card);
    border-radius: 16px;
    border-bottom: 3px solid var(--brand-blue);
    box-shadow: 0 10px 24px rgba(0,0,0,0.18);
    overflow: hidden;
  }
  .wordmark {
    color: var(--brand-blue);
    font-weight: 700;
    letter-spacing: 0.02em;
    line-height: 1;
  }
  .card-front .wordmark {
    position: absolute;
    left: 40px;
    top: 36px;
    font-size: 48px;
  }
  .identity {
    position: absolute;
    left: 40px;
    top: 122px;
  }
  .person-name {
    color: var(--brand-blue);
    font-weight: 700;
    font-size: 25px;
    line-height: 1.15;
  }
  .person-role {
    color: var(--ink);
    font-size: 15px;
    margin-top: 2px;
  }
  .rule {
    position: absolute;
    left: 40px;
    right: 40px;
    top: 192px;
    height: 1.5px;
    background: var(--brand-blue);
  }
  .contacts {
    position: absolute;
    left: 40px;
    top: 204px;
    list-style: none;
    color: var(--ink);
    font-size: 14px;
    line-height: 1.55;
  }
  .contacts li { display: flex; align-items: center; gap: 7px; }
  .contacts svg { width: 12px; height: 12px; fill: var(--brand-blue); flex: none; }
  .address {
    position: absolute;
    right: 40px;
    top: 212px;
    text-align: right;
    color: var(--ink);
    font-size: 14px;
    line-height: 1.55;
    font-style: normal;
  }
  .card-back {
    display: flex;
    align-items: center;
    justify-content: center;
  }
  .card-back .wordmark { font-size: 92px; }
</style>
</head>
<body>
  <section class="card card-front" aria-label="Card front">
    <div class="wordmark">Quendix</div>
    <div class="identity">
      <div class="person-name">Brent Malvoy</div>
      <div class="person-role">General Manager</div>
    </div>
    <div class="rule"></div>
    <ul class="contacts">
      <li>
        <svg viewBox="0 0 24 24" aria-hidden="true"><path d="M6.6 10.8a15.1 15.1 0 0 0 6.6 6.6l2.2-2.2a1 1 0 0 1 1-.25 11.4 11.4 0 0 0 3.6.57 1 1 0 0 1 1 1V20a1 1 0 0 1-1 1A17 17 0 0 1 3 4a1 1 0 0 1 1-1h3.5a1 1 0 0 1 1 1c0 1.25.2 2.45.57 3.57a1 1 0 0 1-.25 1z"/></svg>
        0471 592 304
      </li>
      <li>
        <svg viewBox="0 0 24 24" aria-hidden="true"><path d="M2 5h20v14H2z M2 5l10 8 10-8" stroke="#fff" stroke-width="1.5"/></svg>
        Brent.malvoy@quendix.com.au
      </li>
      <li>
        <svg viewBox="0 0 24 24" aria-hidden="true"><circle cx="12" cy="12" r="10"/><path d="M2 12h20M12 2c3 3 3 17 0 20M12 2c-3 3-3 17 0 20" stroke="#fff" stroke-width="1.3" fill="none"/></svg>
        www.quendix.com.au
      </li>
    </ul>
    <address class="address">87 Harrowgate Ave,<br>Pindarra, QLD, 4000</address>
  </section>

  <section class="card card-back" aria-label="Card back">
    <div class="wordmark">Quendix</div>
  </section>
</body>
</html>
```